practice letterhead

I need a letterhead design for a new company that is a veterinary specialty company. I am conservative. I want it to look professional - not "cutesy"

I need my name, credentials, address, phone number and website/email on it.

My personal information is as follows: Lorraine Aldous, DVM, DACVIM (Neurology) Certified Veterinary Pain Practitioner (or CVPP) Certified Canine Rehabilitation Therapist (or CCRT) 1487 Marden Hwy Halden, NH 02317 508-374-6620 lorraine.aldous@kindpawspecialty.com www.kindpawspecialty.com

```html
<!DOCTYPE html>
<html lang="en">
<head>
<meta charset="utf-8">
<title>Kind Paw Specialty Center – Letterhead</title>
<link href="https://fonts.googleapis.com/css2?family=Source+Sans+3:wght@400;600&display=swap" rel="stylesheet">
<style>
  :root {
    --ink-navy: #1b3540;
    --sage: #6b9487;
    --footer-text: #243a41;
    --paper: #ffffff;
  }
  html, body {
    margin: 0;
    padding: 0;
    overflow: hidden;
    background: var(--paper);
  }
  .letterhead {
    position: relative;
    width: 927px;
    height: 1200px;
    overflow: hidden;
    background: var(--paper);
    font-family: "Source Sans 3", "Myriad Pro", sans-serif;
  }
  .brand {
    position: absolute;
    left: 12px;
    top: 14px;
    display: flex;
    align-items: center;
    gap: 12px;
  }
  .brand-dot {
    width: 56px;
    height: 56px;
    border-radius: 50%;
    background: var(--sage);
    flex: none;
  }
  .brand-name {
    color: var(--sage);
    font-weight: 600;
    font-size: 22px;
    line-height: 25px;
    letter-spacing: 0.3px;
  }
  .credential-band {
    position: absolute;
    left: 323px;
    top: 0;
    right: 0;
    height: 66px;
    background: var(--ink-navy);
  }
  .credential-strip {
    position: absolute;
    left: 323px;
    top: 68px;
    right: 0;
    height: 16px;
    background: var(--sage);
  }
  .credentials {
    position: absolute;
    left: 340px;
    top: 19px;
    margin: 0;
    color: #ffffff;
    font-size: 16.5px;
    line-height: 22px;
    font-weight: 400;
    white-space: nowrap;
  }
  .credentials span { display: block; }
  .footer {
    position: absolute;
    left: 0;
    bottom: 0;
    width: 100%;
    height: 74px;
    background: var(--sage);
    color: var(--footer-text);
    text-align: center;
    font-size: 16.5px;
    line-height: 22px;
    padding-top: 14px;
    box-sizing: border-box;
  }
  .footer p { margin: 0; }
</style>
</head>
<body>
  <main class="letterhead">
    <header>
      <div class="brand">
        <span class="brand-dot" aria-hidden="true"></span>
        <div class="brand-name">Kind Paw<br>Specialty Center</div>
      </div>
      <div class="credential-band"></div>
      <div class="credential-strip"></div>
      <p class="credentials">
        <span>Lorraine Aldous, DVM, DACVIM (Neurology) Certified Veterinary</span>
        <span>Pain Practitioner (or CVPP) Certified Canine Rehabilitation Therapist</span>
        <span>(or CCRT)</span>
      </p>
    </header>
    <footer class="footer">
      <p>1487 Marden Hwy Halden, NH 02317 508-374-6620</p>
      <p>lorraine.aldous@kindpawspecialty.com www.kindpawspecialty.com</p>
    </footer>
  </main>
</body>
</html>
```